Redesign of www.tidewellgallerynews.example.

I need to take the elements of a PixelHive website that was started some time ago but never went live with a website that I now have that is not very compelling. I publish a digital magazine through pagereel.example and link the magazine to www.tidewellgallerynews.example. Boring website.

The PixelHive website is: www.coveharborfunandshows.example. A lively website which is now too narrow in scope. I seek to expand my coverage to include the cultural life of my county.

Here's what I'd like to do.
1. Rename the PixelHive website using my url: www.tidewellgallerynews.example.
2. Use my tidewellgallerynews logo, replacing coveharborfunandshows.example
3. Break up the large rotating banner on the top into two spaces??? I want to feature my current magazine as the first placement. The space is too wide? Suggestions here appreciated. I also want back issues to be available for viewing.
4. I need flexibility to change headings, etc, so instruction needs to come with the design.
5. I'm thinking of offering blog space to others.

General question. Rather than moving everything over to www.coveharborfunandshows.example, should we just redesign www.tidewellgallerynews.example using the elements on the www.coveharborfunandshows.example site? Might be an easier way to go.

I'm open to a complete redesign of www.tidewellgallerynews.example with the exception of the logo and the spotlight on the magazines,both current and past issues.

I am in the middle of producing the next issue, so the website needs to not change until mid October. I'd like the design to be complete beforehand so we can make the change pretty quickly after the 15th of October.

I've attached covers of our last 2 issues and my logo. I'm open to a change in color with the logo,but not the fonts.

I'm not sure how many pages I'll need and I don't know the difference between coded and uncoded pages...so you can explain to me.

Target Market(s)

Readers who are interested in the arts and culture of the San Francisco Bay Area.

Number of Pages Required

4 page

Font styles to use
Other font styles liked:
• Whatever font is used at www.coveharborfunandshows.example

Colors

Designer to choose colors to be used in the design.

Requirements
Must have
• Current logo. Color suggestion for the website is fine.Featured space for the magazines. They are placed by my linking them from Pagereel.example over to my current website. www.coveharborfunandshows should be used as a template.
• WordPress for blogging and instructions included.
Nice to have
• Nice, bright, fun

```html
<!DOCTYPE html>
<html lang="en">
<head>
<meta charset="utf-8">
<title>Tidewell Gallery News</title>
<link href="https://fonts.googleapis.com/css2?family=Mulish:wght@400;600;700&family=Open+Sans:wght@400;600&family=Roboto:wght@400&display=swap" rel="stylesheet">
<style>
:root{
  --yellow:#e5d800;
  --yellow-deep:#d4c200;
  --purple:#7a3b82;
  --purple-dark:#4a1a4e;
  --purple-light:#a56aa8;
  --ink:#222;
  --body:#555;
  --line:#ddd;
  --paper:#fff;
  --mist:#efefef;
}
*{box-sizing:border-box;margin:0;padding:0}
html,body{width:1200px;height:2446px;overflow:hidden}
body{position:relative;background:var(--paper);font-family:"Open Sans",sans-serif;color:var(--body)}
h2,h3{font-weight:400}
.abs{position:absolute}
/* header */
.site-header{left:0;top:0;width:1200px;height:119px}
.brand{left:115px;top:30px;font-family:"Mulish",sans-serif;font-weight:700;font-size:40px;color:var(--yellow-deep);letter-spacing:-.5px;display:flex;align-items:center;gap:12px}
.brand-dot{width:22px;height:22px;border-radius:50%;background:var(--purple)}
.search{left:831px;top:52px;width:242px;height:33px;border:1px solid #bbb;border-radius:17px;font-size:12px;color:#888;padding:8px 16px}
.search svg{position:absolute;right:12px;top:8px}
/* nav */
.main-nav{left:0;top:119px;width:1200px;height:49px;background:var(--yellow)}
.main-nav ul{list-style:none;display:flex;position:absolute;left:115px;top:0;height:49px}
.main-nav li{font-family:"Mulish",sans-serif;font-weight:600;font-size:16px;color:#fff;line-height:49px;padding:0 16px;position:relative}
.main-nav li+li:before{content:"";position:absolute;left:0;top:12px;height:25px;border-left:1px solid rgba(255,255,255,.45);transform:skewX(-20deg)}
.main-nav li.active{background:var(--purple);clip-path:polygon(12px 0,100% 0,calc(100% - 6px) 100%,0 100%);padding:0 28px}
/* hero */
.hero{left:0;top:168px;width:1200px;height:480px;background:var(--yellow);overflow:hidden}
.hero-purple{position:absolute;inset:0;background:linear-gradient(135deg,var(--purple-light) 0%,var(--purple) 45%,var(--purple-dark) 100%);clip-path:polygon(644px 0,1200px 0,1200px 480px,473px 480px)}
.hero-edge{position:absolute;inset:0;background:#b59450;clip-path:polygon(630px 0,644px 0,473px 480px,459px 480px)}
.cover-frame{left:163px;top:44px;width:275px;height:365px;border:10px solid var(--yellow-deep)}
.cover-back{left:186px;top:60px;width:286px;height:370px;background:#f0e200}
.cover{left:182px;top:60px;width:248px;height:330px;background:linear-gradient(160deg,#cfcfcf,#6e6e6e 55%,#3a3a3a);}
.hero-title{left:645px;top:100px;font-family:"Mulish",sans-serif;font-weight:400;font-size:29px;color:#fff;letter-spacing:.5px}
.hero-copy{left:645px;top:154px;width:430px;font-family:"Mulish",sans-serif;font-size:14px;line-height:24px;color:#fff}
.hero-copy p+p{margin-top:14px}
.btn-outline{left:645px;top:341px;width:147px;height:37px;border:2px solid #fff;color:#fff;font-family:"Mulish",sans-serif;font-size:14px;text-align:center;line-height:33px}
.arrow{top:190px}
/* what we do */
.section-title{width:1200px;left:0;text-align:center;font-family:"Mulish",sans-serif;font-weight:400;font-size:30px;color:var(--ink);letter-spacing:.5px}
.intro{left:190px;top:760px;width:820px;text-align:center;font-size:14.5px;line-height:29px}
.intro p+p{margin-top:20px}
/* contributors */
.contributors{left:0;top:997px;width:1200px;height:475px;background:linear-gradient(120deg,var(--yellow) 0%,#c9b51a 30%,#9c6a5a 65%,var(--purple) 100%)}
.card{top:103px;width:231px;height:295px;border:1px solid rgba(255,255,255,.7);text-align:center;color:#fff}
.avatar{width:120px;height:120px;border-radius:50%;border:3px solid #fff;margin:22px auto 0}
.card h3{font-family:"Mulish",sans-serif;font-weight:700;font-size:16px;margin-top:14px}
.card p{font-size:11px;line-height:18px;margin:12px 22px 0}
.dots{left:560px;top:428px;display:flex;gap:6px}
.dots span{width:11px;height:11px;border-radius:50%;background:#fff;border:1px solid #fff}
.dots span:first-child{background:transparent}
/* news */
.news-title{color:var(--purple)}
.news-photo{width:175px;height:175px;border-radius:50%;border:2px solid #bbb;padding:5px}
.news-photo div{width:100%;height:100%;border-radius:50%}
.news h3{font-family:"Roboto",sans-serif;font-weight:400;font-size:19px;line-height:25px;color:var(--ink)}
.news p{font-size:11.5px;line-height:19px;color:#777;margin-top:10px}
.news .more{font-family:"Mulish",sans-serif;font-size:13px;color:var(--purple);margin-top:10px}
/* subscribe */
.subscribe{left:0;top:1868px;width:1200px;height:372px;background:radial-gradient(circle at 80% 20%,#fafafa,var(--mist) 70%)}
.field{width:289px;height:49px;background:#fff;border:1px solid var(--line);box-shadow:0 1px 3px rgba(0,0,0,.08);font-family:"Mulish",sans-serif;font-size:16px;color:#666;padding:13px 18px}
.submit{left:503px;top:260px;width:204px;height:46px;background:var(--yellow-deep);font-family:"Mulish",sans-serif;font-weight:700;font-size:17px;color:#111;text-align:center;line-height:46px}
/* footer */
.site-footer{left:0;top:2240px;width:1200px;height:206px;background:var(--purple);border-top:6px solid var(--yellow)}
.footer-nav{left:0;top:48px;width:1200px;display:flex;justify-content:center;gap:26px;font-family:"Mulish",sans-serif;font-size:16px;color:#fff;list-style:none}
.copyright{left:0;top:86px;width:1200px;text-align:center;font-size:12px;color:#eee}
.social{left:498px;top:122px;display:flex;gap:11px}
.social span{width:40px;height:40px;border:2px solid #fff;border-radius:50%}
</style>
</head>
<body>

<header class="abs site-header">
  <div class="abs brand"><span class="brand-dot"></span>tidewell gallery news</div>
  <div class="abs search">Search here
    <svg width="16" height="16" viewBox="0 0 16 16"><circle cx="6.5" cy="6.5" r="5" fill="none" stroke="#888" stroke-width="2"/><line x1="10" y1="10" x2="15" y2="15" stroke="#888" stroke-width="2"/></svg>
  </div>
</header>

<nav class="abs main-nav">
  <ul>
    <li class="active">Home</li><li>Music</li><li>Art</li><li>Books</li><li>Theatre</li><li>Dance</li><li>Community Events</li><li>Kid Events</li><li>Dining</li><li>Contact Us</li>
  </ul>
</nav>

<section class="abs hero">
  <div class="hero-purple"></div>
  <div class="hero-edge"></div>
  <div class="abs cover-back"></div>
  <div class="abs cover-frame"></div>
  <div class="abs cover" role="img" aria-label="Cover of the current magazine issue featuring an artist at work"></div>
  <h2 class="abs hero-title">ABOUT OUR MAGAZINE</h2>
  <div class="abs hero-copy">
    <p>commodo a mi Morbi ornare gravida elit Integer congue augue et malesuada iaculis ipsum dui aliquet felis at cursus magna nisl nec elit Praesent elementum elit at tellus</p>
    <p>libero interdum nec interdum vel blandit sed nulla In ullamcorper est eget tempor cursus neque mi consectetuer mi a ultricies massa est sed nisl Class aptent taciti sociosq</p>
  </div>
  <div class="abs btn-outline">READ MORE</div>
  <svg class="abs arrow" style="left:80px" width="20" height="40" viewBox="0 0 20 40"><polyline points="16,4 4,20 16,36" fill="none" stroke="#fff" stroke-width="3"/></svg>
  <svg class="abs arrow" style="left:1102px" width="20" height="40" viewBox="0 0 20 40"><polyline points="4,4 16,20 4,36" fill="none" stroke="#fff" stroke-width="3"/></svg>
</section>

<h2 class="abs section-title" style="top:705px">WHAT WE DO</h2>
<div class="abs intro">
  <p>And so we begin with Tidewell Gallery News, an online magazine written for Tidewellers and their friends who love the Arts. We publish 10 times a year, combining July/August and December/January.</p>
  <p>Lawyer by day, jazz pianist by night? School secretary by day, poet by night? Beautiful paintings, hanging in the home of the artist, never seen? I hear these stories all the time. A yearning to create. My passion is to give a voice and expression to everyone, no matter what kind of art form, no matter age.</p>
</div>

<section class="abs contributors">
  <h2 class="abs section-title" style="top:45px;color:#fff;font-size:28px">CONTRIBUTORS</h2>
  <article class="abs card" style="left:127px">
    <div class="avatar" role="img" aria-label="Portrait of Walter Pennick" style="background:linear-gradient(#e8e0d8,#b9a79a)"></div>
    <h3>Walter Pennick</h3>
    <p>Walter Pennick has published several books on history, law, and of poetry. His poetry and legal, literary and historical essays</p>
  </article>
  <article class="abs card" style="left:364px">
    <div class="avatar" role="img" aria-label="Portrait of Delia Marsh" style="background:linear-gradient(#c98a5a,#5a2a18)"></div>
    <h3>Delia Marsh</h3>
    <p>Delia Marsh, owner of Fennel Table in Larkmoor and Pell Cove—a food and wine pairing service working</p>
  </article>
  <article class="abs card" style="left:601px">
    <div class="avatar" role="img" aria-label="Portrait of Rosa Ellery Vance" style="background:linear-gradient(#eeeeee,#9a9a9a)"></div>
    <h3>Rosa Ellery Vance</h3>
    <p>Rosa Ellery Vance focuses her career on supporting projects that build community and increase opportunities for the arts</p>
  </article>
  <article class="abs card" style="left:838px">
    <div class="avatar" role="img" aria-label="Portrait of Calvin Ormsby" style="background:linear-gradient(#8a3a1a,#2a0d06)"></div>
    <h3>Calvin Ormsby</h3>
    <p>Calvin Ormsby is a former weekly syndicated columnist for the Bayline Courier and a winner of the prestigious Harold Lenz</p>
  </article>
  <div class="abs dots"><span></span><span></span><span></span><span></span></div>
</section>

<h2 class="abs section-title news-title" style="top:1538px">LATEST NEWS</h2>
<article class="abs news" style="left:123px;top:1613px;width:440px">
  <div class="news-photo"><div role="img" aria-label="Stage poster with colourful blurred lights" style="background:radial-gradient(circle at 40% 40%,#e8c84a,#b0442a 40%,#1c1c2a 75%)"></div></div>
  <div class="abs" style="left:190px;top:6px;width:250px">
    <h3>Harlow Bandstand at Elm Green</h3>
    <p>The cast of Romeo &amp; Juliet includes Leo Varga* as Romeo, Nell Ashby* as Juliet, Tomas Reid as Mercutio, Omar Bello as Tybalt, Hugh Talbot Jr.—as Lord Capulet, Irene Solis* as Lady Capulet, Dean Holloway</p>
    <div class="more">READ MORE</div>
  </div>
</article>
<article class="abs news" style="left:618px;top:1613px;width:470px">
  <div class="news-photo"><div role="img" aria-label="Portrait of Simone Adair Price" style="background:linear-gradient(#9a9a9a,#3a2418)"></div></div>
  <div class="abs" style="left:200px;top:6px;width:270px">
    <h3>Simone Adair Price*</h3>
    <p>commodo a mi Morbi ornare gravida elit Integer congue augue et malesuada iaculis ipsum dui aliquet felis at cursus magna nisl nec elit Praesent elementum elit at tellus nec ultricies sit amet porttitor mattis enim In massa libero interdum nec interdum vel blandit sed nulla In</p>
    <div class="more">READ MORE</div>
  </div>
</article>

<section class="abs subscribe">
  <h2 class="abs section-title" style="top:52px;font-size:28px">SUBSCRIBE FREE!</h2>
  <div class="abs field" style="left:160px;top:117px">Name</div>
  <div class="abs field" style="left:459px;top:117px">Email</div>
  <div class="abs field" style="left:758px;top:117px">City</div>
  <div class="abs field" style="left:160px;top:182px">State</div>
  <div class="abs field" style="left:459px;top:182px">Zip</div>
  <div class="abs field" style="left:758px;top:182px">Address</div>
  <div class="abs submit">SUBMIT</div>
</section>

<footer class="abs site-footer">
  <ul class="abs footer-nav">
    <li>Home</li><li>Music</li><li>Art</li><li>Books</li><li>Theatre</li><li>Dance</li><li>Community Events</li><li>Kid Events</li><li>Dining</li><li>Contact Us</li>
  </ul>
  <div class="abs copyright">© 2017 Company Name &nbsp;All right reserved &nbsp;Term of Use</div>
  <div class="abs social"><span></span><span></span><span></span><span></span></div>
</footer>

</body>
</html>
```